Builder of high-end, expensive tables and other furniture

Build a website that represents what we do. I want a luxury feel that appeals to those who can afford our products. We build very high end tables and other furniture using trees that have fallen or are standing dead. We never cut living trees. Trees are harvested, milled, and kiln dried. Then that lumber is meticulously turned into fine furniture using the best equipment. Our furniture prices range from $1,000-$20,000.

Trying to figure out how to raise my spend.

```html
<!DOCTYPE html>
<html lang="en">
<head>
<meta charset="utf-8">
<title>Timberfall Tables — Fine Furniture From Fallen Timber</title>
<link href="https://fonts.googleapis.com/css2?family=Figtree:wght@400;500;600;700&family=Playfair+Display:wght@700&display=swap" rel="stylesheet">
<style>
:root{
  --blue:#0456b0;
  --orange:#f07a26;
  --ink:#1c1c1c;
  --muted:#555;
  --white:#fff;
  --soft:#f4f4f4;
  --card-warm:#f8efe8;
  --card-grey:#efefed;
  --card-light:#f1f1ef;
}
*{box-sizing:border-box;margin:0;padding:0}
html,body{width:1200px;height:4304px;overflow:hidden;background:var(--white)}
body{font-family:"Figtree",sans-serif;color:var(--ink);position:relative}
a{color:inherit;text-decoration:none}
.abs{position:absolute}
section,header,footer{position:absolute;left:0;width:1200px}

/* header */
.site-header{top:0;height:84px;background:var(--white)}
.brand{left:142px;top:22px;font-size:30px;font-weight:600;color:var(--orange);display:flex;align-items:center;gap:8px}
.brand .dot{width:12px;height:12px;border-radius:50%;background:var(--orange)}
.nav{top:34px;font-size:11px;font-weight:500;letter-spacing:.3px}
.nav.active{color:var(--orange)}
.divider-v{left:968px;top:24px;width:1px;height:36px;background:#ddd}
.cart-total{left:1016px;top:34px;font-size:11px;font-weight:600}

/* hero */
.hero{top:84px;height:551px}
.hero-photo{position:absolute;inset:0;background:linear-gradient(100deg,#3b3a36 0%,#5f5d56 40%,#8a8578 65%,#4a4a3c 100%)}
.hero-kicker{left:142px;top:107px;font-size:12px;font-weight:600;color:var(--white)}
.hero-title{left:140px;top:122px;font-family:"Playfair Display",serif;font-size:82px;line-height:92px;color:var(--white);letter-spacing:1px}
.hero-text{left:142px;top:317px;width:470px;font-size:14px;line-height:20px;color:var(--white)}
.btn-ghost{left:142px;top:402px;width:114px;height:39px;border:2px solid var(--white);color:var(--white);font-size:12px;font-weight:600;display:flex;align-items:center;justify-content:center}

/* shared */
.sec-title{width:1200px;left:0;text-align:center;font-size:30px;font-weight:700;color:var(--blue)}
.sec-title .hl{color:var(--orange)}
.sec-sub{width:1200px;left:0;text-align:center;font-size:13px;color:var(--ink)}
.btn-outline{height:41px;border:2px solid var(--orange);color:var(--blue);font-size:12px;font-weight:700;display:flex;align-items:center;justify-content:center}
.photo{position:absolute}

/* arrivals */
.arrivals{top:635px;height:739px}
.product{width:292px}
.product .photo{left:0;top:0;width:292px;height:309px}
.tag{position:absolute;right:6px;top:7px;background:var(--orange);color:var(--white);font-size:10px;padding:4px 12px}
.product h3{position:absolute;top:334px;font-size:20px;font-weight:600}
.price{position:absolute;top:360px;font-size:16px;color:var(--muted);white-space:nowrap}
.price s{font-style:italic;margin-left:8px;color:#888}
.add-cart{position:absolute;top:399px;font-size:11px;font-weight:700;display:flex;align-items:center;gap:6px;white-space:nowrap}

/* rooms */
.rooms{top:1374px;height:1178px;background:var(--blue);color:var(--white)}
.rooms .sec-title{color:var(--white)}
.rooms .sec-sub{color:var(--white)}
.room-photo{width:446px;height:269px}
.room-text{width:350px}
.room-text h3{font-size:21px;font-weight:600}
.room-text p{margin-top:14px;font-size:12px;line-height:22px}
.room-text a{display:inline-block;margin-top:14px;font-size:12px;font-weight:700;text-decoration:underline}

/* category */
.category{top:2552px;height:658px}
.cat-card{width:292px;height:323px}
.cat-card span{position:absolute;left:0;right:0;top:22px;text-align:center;font-size:24px;font-weight:500}
.cat-card .photo{left:30px;right:30px;top:80px;bottom:40px;border-radius:6px}

/* blogs */
.blogs{top:3210px;height:760px;background:var(--soft)}
.post-thumb{width:122px;height:125px}
.post{width:290px}
.post time{font-size:13px;color:var(--blue)}
.post h4{margin-top:7px;font-size:17px;line-height:23px;font-weight:600}
.post p{margin-top:8px;font-size:13px;line-height:22px}
.feature-photo{left:625px;top:172px;width:434px;height:268px}
.date-badge{left:983px;top:394px;width:55px;height:55px;background:var(--orange);color:var(--white);text-align:center;font-size:9px;line-height:10px;padding-top:6px}
.date-badge b{display:block;font-size:18px;line-height:18px;font-weight:500}
.feature-text{left:625px;top:460px;width:434px}
.feature-text h3{font-size:20px;line-height:29px;font-weight:500}
.feature-text p{margin-top:10px;font-size:13px;line-height:22px}
.read-more{display:flex;align-items:center;gap:8px;margin-top:12px;font-size:12px;font-weight:700}

/* footer */
.site-footer{top:3970px;height:334px;background:var(--blue);color:var(--white)}
.foot-brand{left:142px;top:68px;font-size:28px;font-weight:600;display:flex;align-items:center;gap:8px}
.foot-brand .dot{width:11px;height:11px;border-radius:50%;background:var(--white)}
.foot-about{left:142px;top:112px;width:300px;font-size:12px;line-height:19px}
.social{top:202px;width:24px;height:24px;border-radius:50%;border:1px solid var(--white)}
.foot-col h5{font-size:15px;font-weight:600}
.foot-col ul{list-style:none;margin-top:12px}
.foot-col li{font-size:12px;line-height:23px}
.foot-news{left:784px;top:84px;width:272px}
.foot-news p{margin-top:12px;font-size:12px;line-height:19px}
.subscribe{margin-top:16px;display:flex;height:35px;background:var(--white)}
.subscribe span{flex:1;display:flex;align-items:center;gap:10px;padding-left:18px;font-size:12px;color:#555}
.subscribe b{width:72px;background:var(--orange);color:var(--white);font-size:11px;display:flex;align-items:center;justify-content:center}
.copyright{left:0;width:1200px;top:298px;text-align:center;font-size:12px}
</style>
</head>
<body>

<header class="site-header">
  <a class="brand abs" href="#"><span class="dot"></span>Timberfall Tables</a>
  <a class="nav active abs" style="left:533px" href="#">HOME</a>
  <a class="nav abs" style="left:602px" href="#">ABOUT US</a>
  <a class="nav abs" style="left:692px" href="#">SHOP</a>
  <a class="nav abs" style="left:759px" href="#">BLOG</a>
  <a class="nav abs" style="left:826px" href="#">CONTACT US</a>
  <svg class="abs" style="left:932px;top:33px" width="16" height="16" viewBox="0 0 16 16" aria-label="Search"><circle cx="6.5" cy="6.5" r="4.8" fill="none" stroke="#0456b0" stroke-width="2"/><path d="M10 10l4 4" stroke="#0456b0" stroke-width="2.2" stroke-linecap="round"/></svg>
  <div class="divider-v abs"></div>
  <svg class="abs" style="left:995px;top:28px" width="16" height="20" viewBox="0 0 16 20" aria-label="Cart"><rect x="1.5" y="6" width="13" height="12.5" fill="none" stroke="#f07a26" stroke-width="1.6"/><path d="M5 8V4.5a3 3 0 0 1 6 0V8" fill="none" stroke="#f07a26" stroke-width="1.6"/></svg>
  <span class="cart-total abs">$4,850.00</span>
</header>

<section class="hero">
  <div class="hero-photo" role="img" aria-label="Living room with a grey sofa, round white coffee table, rattan pendant lamps and potted plants"></div>
  <p class="hero-kicker abs">Heirloom Furniture From Fallen And Standing Dead Trees</p>
  <h1 class="hero-title abs">MODERN<br>FURNITURE</h1>
  <p class="hero-text abs">Fine tables made only from trees that have fallen or stand dead. We never cut a living tree. Each log is milled, kiln dried and crafted by hand into a piece that lasts.</p>
  <a class="btn-ghost abs" href="#">SHOP NOW</a>
</section>

<section class="arrivals">
  <h2 class="sec-title abs" style="top:77px"><span class="hl">New</span> Arrivals</h2>
  <p class="sec-sub abs" style="top:121px">Our latest pieces, each made from reclaimed fallen timber</p>

  <article class="product abs" style="left:142px;top:162px">
    <div class="photo" role="img" aria-label="Round solid wood dining table on a pale grey background" style="background:linear-gradient(180deg,#e9eaec,#dcdde0)"></div>
    <span class="tag">Sale</span>
    <h3>Expensive Tables</h3>
    <p class="price">$ 4,850.00 USD <s>$ 5,600.00 USD</s></p>
    <a class="add-cart" href="#">ADD TO CART <svg width="14" height="8" viewBox="0 0 14 8"><path d="M0 4h12M9 1l3 3-3 3" fill="none" stroke="#f07a26" stroke-width="1.2"/></svg></a>
  </article>
  <article class="product abs" style="left:455px;top:162px">
    <div class="photo" role="img" aria-label="Grey fabric sofa with white cushion" style="background:linear-gradient(180deg,#ececea,#d9d9d5)"></div>
    <h3>Ostrow</h3>
    <p class="price">$ 7,200.00 USD <s>$ 8,400.00 USD</s></p>
    <a class="add-cart" href="#">ADD TO CART <svg width="14" height="8" viewBox="0 0 14 8"><path d="M0 4h12M9 1l3 3-3 3" fill="none" stroke="#f07a26" stroke-width="1.2"/></svg></a>
  </article>
  <article class="product abs" style="left:767px;top:162px">
    <div class="photo" role="img" aria-label="Wooden side table with book shelf" style="background:linear-gradient(180deg,#eeeeec,#e0ddd8)"></div>
    <span class="tag">Sale</span>
    <h3>Elmshore</h3>
    <p class="price">$ 1,950.00 USD <s>$ 2,400.00 USD</s></p>
    <a class="add-cart" href="#">ADD TO CART <svg width="14" height="8" viewBox="0 0 14 8"><path d="M0 4h12M9 1l3 3-3 3" fill="none" stroke="#f07a26" stroke-width="1.2"/></svg></a>
  </article>

  <a class="btn-outline abs" style="left:541px;top:612px;width:116px" href="#">SHOP NOW</a>
</section>

<section class="rooms">
  <h2 class="sec-title abs" style="top:78px"><span class="hl">Decorate By</span> Room</h2>
  <p class="sec-sub abs" style="top:122px">Furnish every room with pieces born from fallen trees</p>

  <div class="photo room-photo" style="left:142px;top:173px;background:linear-gradient(180deg,#e6e6e4,#b9b9b6)" role="img" aria-label="Bright living room with grey sofa and glass coffee table"></div>
  <div class="room-text abs" style="left:670px;top:238px">
    <h3>Living Room Set</h3>
    <p>Coffee tables and consoles cut from windfall oak and walnut, kiln dried for stability and finished by hand to show every ring of the tree.</p>
    <a href="#">VIEW MORE</a>
  </div>

  <div class="room-text abs" style="left:185px;top:565px">
    <h3>Bedroom Set</h3>
    <p>Beds, nightstands and dressers built from standing dead timber, joined with traditional methods so each piece can pass down for generations.</p>
    <a href="#">VIEW MORE</a>
  </div>
  <div class="photo room-photo" style="left:610px;top:499px;background:linear-gradient(180deg,#d8cfc2,#a99886)" role="img" aria-label="Bedroom with cream bedding and large window"></div>

  <div class="photo room-photo" style="left:142px;top:823px;background:linear-gradient(180deg,#e3d6c6,#b7a58e)" role="img" aria-label="Lounge area with white armchairs and black floor lamp"></div>
  <div class="room-text abs" style="left:670px;top:887px">
    <h3>Other Furniture</h3>
    <p>Benches, desks and commissioned pieces from $1,000 to $20,000, each one milled from a single reclaimed log and made with precision tools.</p>
    <a href="#">VIEW MORE</a>
  </div>
</section>

<section class="category">
  <h2 class="sec-title abs" style="top:78px"><span class="hl">Shop by</span> Category</h2>
  <p class="sec-sub abs" style="top:120px">Explore our handcrafted collections by type of piece</p>

  <div class="cat-card abs" style="left:142px;top:170px;background:var(--card-warm)">
    <span>Chair</span>
    <div class="photo" role="img" aria-label="Wooden chair with white seat" style="background:linear-gradient(180deg,#f1e2d3,#e6cdb3)"></div>
  </div>
  <div class="cat-card abs" style="left:453px;top:170px;background:var(--card-grey)">
    <span>Table</span>
    <div class="photo" role="img" aria-label="Round wooden table" style="background:linear-gradient(180deg,#e8e3dc,#d6c3a9)"></div>
  </div>
  <div class="cat-card abs" style="left:766px;top:170px;background:var(--card-light)">
    <span>Sofa</span>
    <div class="photo" role="img" aria-label="Light grey sofa with yellow cushion" style="background:linear-gradient(180deg,#e6e5e2,#cfcecb)"></div>
  </div>

  <a class="btn-outline abs" style="left:542px;top:531px;width:116px" href="#">VIEW ALL</a>
</section>

<section class="blogs">
  <h2 class="sec-title abs" style="top:80px"><span class="hl">Our</span> Blogs</h2>
  <p class="sec-sub abs" style="top:122px">Stories from the forest floor to the finished piece in your home</p>

  <div class="photo post-thumb" style="left:142px;top:174px;background:linear-gradient(180deg,#c89a78,#8a5a3a)" role="img" aria-label="Leather lounge chair"></div>
  <article class="post abs" style="left:287px;top:175px">
    <time>May 23, 2023</time>
    <h4>Why We Only Build With Fallen And Dead Trees</h4>
    <p>No living tree is ever cut. Here is how we find and recover our timber.</p>
  </article>
  <div class="photo post-thumb" style="left:142px;top:319px;background:linear-gradient(180deg,#bfc3c7,#6e7378)" role="img" aria-label="Grey bedroom interior"></div>
  <article class="post abs" style="left:287px;top:320px">
    <time>May 23, 2023</time>
    <h4>Inside The Kiln: Drying Lumber For A Lifetime</h4>
    <p>Slow, careful drying keeps every slab true and stable for decades.</p>
  </article>
  <div class="photo post-thumb" style="left:142px;top:464px;background:linear-gradient(180deg,#ece8e2,#c8b191)" role="img" aria-label="Living room with wooden coffee table"></div>
  <article class="post abs" style="left:287px;top:465px">
    <time>May 23, 2023</time>
    <h4>Caring For A Solid Wood Heirloom Table</h4>
    <p>Simple habits that keep a hand-oiled finish rich for generations.</p>
  </article>

  <div class="photo feature-photo" role="img" aria-label="Family carrying a white armchair into a new home" style="background:linear-gradient(180deg,#dcd8d2,#bdb6ac)"></div>
  <div class="date-badge abs"><b>23</b>MAY<br>2023</div>
  <div class="feature-text abs">
    <h3>From A Storm-Felled Walnut To A Dining Table Built To Last A Century</h3>
    <p>Follow one tree through milling, kiln drying and months of careful joinery to a finished heirloom piece.</p>
    <a class="read-more" href="#">READ MORE <svg width="14" height="8" viewBox="0 0 14 8"><path d="M0 4h12M9 1l3 3-3 3" fill="none" stroke="#f07a26" stroke-width="1.2"/></svg></a>
  </div>

  <a class="btn-outline abs" style="left:542px;top:633px;width:116px" href="#">VIEW ALL</a>
</section>

<footer class="site-footer">
  <a class="foot-brand abs" href="#"><span class="dot"></span>Timberfall Tables</a>
  <p class="foot-about abs">We build fine tables and furniture from trees that have fallen or stand dead. Every log is milled, kiln dried and crafted by hand. We never cut a living tree.</p>
  <span class="social abs" style="left:142px"></span>
  <span class="social abs" style="left:174px"></span>
  <span class="social abs" style="left:206px"></span>
  <span class="social abs" style="left:240px"></span>

  <div class="foot-col abs" style="left:495px;top:84px">
    <h5>Shop</h5>
    <ul><li>All</li><li>Sale</li><li>Living</li><li>Bedroom</li><li>Kitchen</li></ul>
  </div>
  <div class="foot-col abs" style="left:610px;top:84px">
    <h5>Links</h5>
    <ul><li>About</li><li>Blog</li><li>Contact Us</li><li>FAQs</li><li>Terms &amp; Conditions</li></ul>
  </div>
  <div class="foot-news abs">
    <h5 style="font-size:15px;font-weight:600">Join our newsletter</h5>
    <p>Subscribe To Our Newsletter To Get The Latest Update To Your Inbox</p>
    <div class="subscribe">
      <span><svg width="14" height="10" viewBox="0 0 14 10"><rect x=".5" y=".5" width="13" height="9" fill="none" stroke="#777"/><path d="M.5 .5l6.5 5 6.5-5" fill="none" stroke="#777"/></svg>Enter Email</span>
      <b>SUBMIT</b>
    </div>
  </div>
  <p class="copyright abs">© 2023 Timberfall Tables. All Rights Reserved.</p>
</footer>

</body>
</html>
```